BUSINESS CARD - HALLORAN FIELD SERVICES

I would like to create a business card for my fertilizer spreading business. I would like to incorporate my existing logo and also a description of the services offered. The business card will be given to farmers so must be kept simple but effective. It will also be left in stores so much also be eye catching in order to stand out from other cards.

Target Market(s)

FARMERS

Requirements
Must have
• FRONT OF CARD = EXISTING LOGO + "CUSTOMISED SPREADING" below the logo

REAR Of CARD = SERVICES OFFERED AND CONTACT DETAILS

- Bulk fertilizer including Lime, Gypsum, Manure & Compost
- Granular fertilizer including Single Super, Urea, Gran-plus, & Custom Blends
- Modern equipment - Autosteer & Variable Rate Capable
- Friendly & Reliable Service
- Contact Gus: 0471 592 318
Nice to have
• utilize same color scheme as existing logo

```html
<!DOCTYPE html>
<html lang="en">
<head>
<meta charset="utf-8">
<title>Halloran Field Services – Business Card</title>
<link rel="stylesheet" href="https://fonts.googleapis.com/css2?family=Poppins:wght@500;600;700&family=Open+Sans:wght@600&display=swap">
<style>
  :root {
    --page-bg: #f3f3f3;
    --front-grey: #767676;
    --front-grey-dark: #6c6c6c;
    --card-white: #f7f7f7;
    --band-grey: #6f6f6f;
    --panel-black: #161616;
    --accent-orange: #f2a231;
    --brand-grey: #5a5a5a;
    --text-white: #ffffff;
  }
  html, body {
    margin: 0;
    width: 1200px;
    height: 1200px;
    overflow: hidden;
    background: var(--page-bg);
  }
  .canvas {
    position: relative;
    width: 1200px;
    height: 1200px;
  }
  .card {
    position: absolute;
    left: 220px;
    width: 760px;
    height: 436px;
    overflow: hidden;
  }
  /* Front */
  .card-front {
    top: 130px;
    background: linear-gradient(135deg, var(--front-grey), var(--front-grey-dark));
    text-align: center;
  }
  .brand-dot {
    position: absolute;
    left: 50%;
    width: 104px;
    height: 104px;
    border-radius: 50%;
  }
  .card-front .brand-dot {
    top: 110px;
    margin-left: -52px;
    background: var(--text-white);
  }
  .brand-name {
    position: absolute;
    left: 0;
    right: 0;
    font-family: "Poppins", sans-serif;
    font-weight: 600;
    margin: 0;
    white-space: nowrap;
  }
  .card-front .brand-name {
    top: 236px;
    font-size: 32px;
    color: var(--text-white);
  }
  .tagline {
    position: absolute;
    left: 0;
    right: 0;
    top: 308px;
    margin: 0;
    font-family: "Poppins", sans-serif;
    font-weight: 600;
    font-size: 22px;
    letter-spacing: 5px;
    color: var(--accent-orange);
  }
  /* Back */
  .card-back {
    top: 680px;
    background: var(--panel-black);
  }
  .back-shapes {
    position: absolute;
    inset: 0;
  }
  .back-brand {
    position: absolute;
    left: 0;
    top: 0;
    width: 360px;
    height: 436px;
    text-align: center;
  }
  .back-brand .brand-dot {
    top: 112px;
    margin-left: -46px;
    width: 92px;
    height: 92px;
    background: var(--brand-grey);
  }
  .back-brand .brand-name {
    top: 230px;
    font-size: 23px;
    color: var(--brand-grey);
  }
  .services {
    position: absolute;
    left: 438px;
    top: 88px;
  }
  .services-title {
    margin: 0 0 14px 6px;
    font-family: "Poppins", sans-serif;
    font-weight: 600;
    font-size: 20px;
    letter-spacing: 2px;
    color: var(--text-white);
  }
  .services-list {
    margin: 0;
    font-family: "Open Sans", sans-serif;
    font-weight: 600;
    font-size: 16.5px;
    line-height: 25px;
    color: var(--accent-orange);
    white-space: pre;
  }
  .contact {
    position: absolute;
    left: 436px;
    top: 356px;
    display: flex;
    align-items: center;
    gap: 10px;
    font-family: "Poppins", sans-serif;
    font-weight: 600;
    font-size: 19px;
    color: var(--text-white);
    margin: 0;
  }
  .contact svg { width: 22px; height: 22px; }
</style>
</head>
<body>
<main class="canvas">
  <section class="card card-front" aria-label="Card front">
    <span class="brand-dot"></span>
    <h1 class="brand-name">Halloran Field Services</h1>
    <p class="tagline">CUSTOMISED SPREADING</p>
  </section>

  <section class="card card-back" aria-label="Card back">
    <svg class="back-shapes" width="760" height="436" viewBox="0 0 760 436" aria-hidden="true">
      <path d="M0 0 H372 Q418 218 372 436 H0 Z" fill="var(--band-grey)"/>
      <path d="M0 0 H296 Q356 218 300 436 H0 Z" fill="var(--card-white)"/>
    </svg>

    <div class="back-brand">
      <span class="brand-dot"></span>
      <h2 class="brand-name">Halloran Field Services</h2>
    </div>

    <div class="services">
      <h3 class="services-title">SERVICES OFFERED</h3>
<p class="services-list">  Bulk fertilizer including Lime,
  Gypsum,
  Manure &amp; Composts
- Granular fertilizer including
  Single Super,
  Urea, Gran-plus, &amp; Custom Blends
- Modern equipment
- Friendly &amp; Reliable Services</p>
    </div>

    <p class="contact">
      <svg viewBox="0 0 24 24" aria-hidden="true"><path fill="var(--accent-orange)" d="M6.6 10.8a15.1 15.1 0 0 0 6.6 6.6l2.2-2.2a1 1 0 0 1 1-.25 11.4 11.4 0 0 0 3.6.57 1 1 0 0 1 1 1V20a1 1 0 0 1-1 1A17 17 0 0 1 3 4a1 1 0 0 1 1-1h3.5a1 1 0 0 1 1 1c0 1.25.2 2.45.57 3.57a1 1 0 0 1-.25 1z"/></svg>
      <span class="phone-number">0471 592 318</span>
    </p>
  </section>
</main>
</body>
</html>
```